Single page 8 1/2 x 11 flyer to entice new homeowners to visit our WEBSITE

A single page flyer that we can put on an easel that promotes our website, tallowpine58.com, to new homeowners for blinds, shades, bath hardware, cabinet organization, etc. This piece will be on an easel in sales centers, design studios and closing offices. We want the homeowners to know where they can go to get reliable products and service from a trusted partner of their builder for products that were not installed in their new home before they closed.

Enter the coupon code KQT10 to get 10% off of your entire purchase and free shipping. The product on our website will put the finishing touches on their home. ....make your house your home

Target Market(s)

New homebuyers

Industry/Entity Type

Residential Construction

Font styles to use
Serif

Colors
ec1f27

Requirements
Must have
• Logo and website, tallowpine58.com and tagline, make your house your home
Nice to have
• what will drive new homeowners to the website to purchase items they did not purchase before closing like window blinds and shades, bath hardware, ceiling fans, grills, electric fireplaces, etc.

```html
<!DOCTYPE html>
<html lang="en">
<head>
<meta charset="utf-8">
<title>Tallow Pine 58 – Flyer</title>
<link rel="stylesheet" href="https://fonts.googleapis.com/css2?family=Open+Sans:wght@400;600;700;800&family=Noto+Serif:ital,wght@1,700&display=swap">
<style>
  :root{
    --brand-red:#ec1f27;
    --ink:#2b2b2b;
    --paper:#f7f7f5;
    --backdrop:#dfe4ea;
    --footer-dark:#1f1f1f;
  }
  *{box-sizing:border-box;margin:0;padding:0}
  html,body{width:1200px;height:800px;overflow:hidden}
  body{background:var(--backdrop);font-family:"Open Sans",Arial,sans-serif;color:var(--ink);position:relative}
  .flyer{position:absolute;left:320px;top:30px;width:560px;height:740px;background:var(--paper);overflow:hidden;box-shadow:0 6px 24px rgba(0,0,0,.18)}
  .hero{position:absolute;left:0;top:0;width:560px;height:340px;
    background:linear-gradient(180deg,#d9dcdc 0%,#c7cfcf 35%,#a9c4c1 55%,#cfd1cd 75%,#b9b4ab 100%)}
  .hero-accent{position:absolute;right:40px;top:160px;width:110px;height:70px;border-radius:8px;background:rgba(220,50,40,.35)}
  .brand{position:absolute;left:22px;top:22px;display:flex;align-items:center;gap:10px}
  .brand-dot{width:34px;height:34px;border-radius:50%;background:var(--brand-red)}
  .brand-name{font-weight:800;font-size:26px;color:#333;letter-spacing:-.3px}
  .tagline{position:absolute;left:124px;top:292px;color:#fff;font-weight:800;font-size:24px;letter-spacing:1px;white-space:nowrap;text-shadow:0 1px 3px rgba(0,0,0,.35)}
  .offer-badge{position:absolute;left:20px;top:272px;width:100px;height:100px;border-radius:50%;background:#fff;border:4px solid var(--brand-red);
    display:flex;flex-direction:column;align-items:center;justify-content:center;font-family:"Noto Serif",Georgia,serif;font-style:italic;font-weight:700;color:var(--brand-red);line-height:1;z-index:2}
  .offer-badge .pct{font-size:32px}
  .offer-badge .off{font-size:28px}
  .offer-band{position:absolute;left:0;top:340px;width:560px;height:78px;background:var(--brand-red);color:#fff;
    font-family:"Noto Serif",Georgia,serif;font-style:italic;font-weight:700;font-size:15px;line-height:1.35;padding:12px 16px 0 132px}
  .services{position:absolute;left:30px;top:432px;width:500px}
  .services-intro{font-size:11.5px;color:var(--ink);padding-bottom:5px;border-bottom:1px solid #999;display:inline-block;white-space:nowrap;width:340px}
  .services-intro em{font-style:normal;color:var(--brand-red)}
  .service-cols{display:flex;justify-content:space-between;align-items:flex-start;margin-top:8px}
  .service-list{list-style:none;font-size:11px;text-transform:uppercase;color:#333}
  .service-list li{display:flex;align-items:center;gap:6px;height:20px;white-space:nowrap}
  .service-list svg{width:11px;height:11px;flex:none}
  .service-list.c1{margin-top:18px}
  .service-list.c2{margin-top:8px}
  .service-list.c3{margin-top:0}
  .finishing{position:absolute;left:0;width:560px;top:548px;text-align:center;color:var(--brand-red);font-weight:700;font-size:18px;line-height:24px}
  .products{position:absolute;left:26px;top:580px;width:508px;display:flex;justify-content:space-between}
  .product{width:118px;text-align:center}
  .product-photo{width:90px;height:90px;margin:0 auto;border-radius:50%;border:4px solid var(--brand-red)}
  .product-photo.blinds{background:linear-gradient(180deg,#c98a45,#a5652c)}
  .product-photo.hardware{background:radial-gradient(circle,#f2f2f2 40%,#cfcfcf 70%,#e9e9e9)}
  .product-photo.lighting{background:linear-gradient(180deg,#d8cbb6,#8c6a48)}
  .product-photo.organization{background:linear-gradient(180deg,#4b4f57,#2b2e33)}
  .product-label{margin-top:5px;font-size:11px;line-height:15px;text-transform:uppercase;color:#333;white-space:nowrap}
  .footer{position:absolute;left:0;bottom:0;width:560px;height:40px;display:flex}
  .footer-phone{width:200px;background:var(--footer-dark);color:#fff;display:flex;align-items:center;justify-content:center;gap:8px;font-weight:600;font-size:17px}
  .footer-web{flex:1;background:var(--brand-red);color:#fff;display:flex;align-items:center;justify-content:center;gap:10px;font-weight:700;font-size:18px;letter-spacing:.5px}
  .footer svg{width:18px;height:18px}
</style>
</head>
<body>
<main class="flyer">
  <div class="hero" role="img" aria-label="Photo of a bright modern living room with a white sofa, glass partitions and red dining chairs"></div>
  <div class="hero-accent" aria-hidden="true"></div>

  <div class="brand">
    <span class="brand-dot" aria-hidden="true"></span>
    <span class="brand-name">TALLOW PINE 58</span>
  </div>

  <h1 class="tagline">MAKE YOUR HOUSE YOUR HOME</h1>

  <div class="offer-badge"><span class="pct">10%</span><span class="off">off</span></div>

  <p class="offer-band">All purchases made through the website will include free shipping and a 10% discount off of the entire purchase.</p>

  <section class="services">
    <p class="services-intro">We do All Types of <em>HOME DECORATION</em> and <em>RENOVATIONS</em></p>
    <div class="service-cols">
      <ul class="service-list c1">
        <li><svg viewBox="0 0 12 12"><rect x=".5" y=".5" width="11" height="11" fill="none" stroke="#ec1f27"/><path d="M2.5 6l2.5 2.5 5-6" fill="none" stroke="#ec1f27" stroke-width="2"/></svg>Blinds</li>
        <li><svg viewBox="0 0 12 12"><rect x=".5" y=".5" width="11" height="11" fill="none" stroke="#ec1f27"/><path d="M2.5 6l2.5 2.5 5-6" fill="none" stroke="#ec1f27" stroke-width="2"/></svg>Shades</li>
        <li><svg viewBox="0 0 12 12"><rect x=".5" y=".5" width="11" height="11" fill="none" stroke="#ec1f27"/><path d="M2.5 6l2.5 2.5 5-6" fill="none" stroke="#ec1f27" stroke-width="2"/></svg>Bath Hardware</li>
      </ul>
      <ul class="service-list c2">
        <li><svg viewBox="0 0 12 12"><rect x=".5" y=".5" width="11" height="11" fill="none" stroke="#ec1f27"/><path d="M2.5 6l2.5 2.5 5-6" fill="none" stroke="#ec1f27" stroke-width="2"/></svg>Ceiling Fans</li>
        <li><svg viewBox="0 0 12 12"><rect x=".5" y=".5" width="11" height="11" fill="none" stroke="#ec1f27"/><path d="M2.5 6l2.5 2.5 5-6" fill="none" stroke="#ec1f27" stroke-width="2"/></svg>Organization</li>
        <li><svg viewBox="0 0 12 12"><rect x=".5" y=".5" width="11" height="11" fill="none" stroke="#ec1f27"/><path d="M2.5 6l2.5 2.5 5-6" fill="none" stroke="#ec1f27" stroke-width="2"/></svg>Cabinet Hardware</li>
      </ul>
      <ul class="service-list c3">
        <li><svg viewBox="0 0 12 12"><rect x=".5" y=".5" width="11" height="11" fill="none" stroke="#ec1f27"/><path d="M2.5 6l2.5 2.5 5-6" fill="none" stroke="#ec1f27" stroke-width="2"/></svg>Fireplaces</li>
        <li><svg viewBox="0 0 12 12"><rect x=".5" y=".5" width="11" height="11" fill="none" stroke="#ec1f27"/><path d="M2.5 6l2.5 2.5 5-6" fill="none" stroke="#ec1f27" stroke-width="2"/></svg>Lighting</li>
        <li><svg viewBox="0 0 12 12"><rect x=".5" y=".5" width="11" height="11" fill="none" stroke="#ec1f27"/><path d="M2.5 6l2.5 2.5 5-6" fill="none" stroke="#ec1f27" stroke-width="2"/></svg>Outdoor</li>
      </ul>
    </div>
  </section>

  <h2 class="finishing">Put the finishing touch on your new home</h2>

  <section class="products">
    <figure class="product"><div class="product-photo blinds" role="img" aria-label="Photo of wooden window blinds"></div><figcaption class="product-label">Blinds &amp; Shades</figcaption></figure>
    <figure class="product"><div class="product-photo hardware" role="img" aria-label="Photo of a chrome towel ring"></div><figcaption class="product-label">Bath Hardware</figcaption></figure>
    <figure class="product"><div class="product-photo lighting" role="img" aria-label="Photo of pendant lights over a kitchen island"></div><figcaption class="product-label">Lighting</figcaption></figure>
    <figure class="product"><div class="product-photo organization" role="img" aria-label="Photo of a cabinet with pull-out organizer"></div><figcaption class="product-label">Organization</figcaption></figure>
  </section>

  <footer class="footer">
    <div class="footer-phone">
      <svg viewBox="0 0 24 24"><circle cx="12" cy="12" r="10.5" fill="none" stroke="#fff" stroke-width="1.5"/><path d="M9 6.5c-1.5 1-2 2.5-1 5s3 4.5 5 5.5 3 0 4-1l-2-2-1.5 1c-1-.5-2.5-2-3-3l1-1.5z" fill="#fff"/></svg>
      (555) 304-2718
    </div>
    <div class="footer-web">
      <svg viewBox="0 0 24 24" fill="none" stroke="#fff" stroke-width="1.6"><circle cx="12" cy="12" r="10"/><ellipse cx="12" cy="12" rx="4.5" ry="10"/><path d="M2 12h20M4 6.5h16M4 17.5h16"/></svg>
      www.tallowpine58.com
    </div>
  </footer>
</main>
</body>
</html>
```